Financial Services Sales Sheet

We need this sheet redesigned. Needs to feel very corporate/financial. open to imagery/icons/colors/etc. Copy is in the docx file to expedite work. PDF is what client has done inh-house and feels dated.

```html
<!DOCTYPE html>
<html lang="en">
<head>
<meta charset="utf-8">
<title>Harbor Crest Portfolio Advisors – Master Servicing &amp; Portfolio Optimization</title>
<link href="https://fonts.googleapis.com/css2?family=Archivo:wght@600;700;800;900&family=Barlow:wght@800;900&family=Inter:wght@400;500;600;700&family=Montserrat:wght@600;700;800&display=swap" rel="stylesheet">
<style>
:root{
  --navy:#0b1f4a;
  --navy-deep:#071330;
  --band:#0a1838;
  --ink:#1d2430;
  --grey:#5c6571;
  --blue:#1f6fde;
  --blue-bright:#3d8bff;
  --line:#d7dce4;
  --white:#ffffff;
  --muted:#b7c3d8;
}
*{margin:0;padding:0;box-sizing:border-box}
html,body{width:800px;height:1200px;overflow:hidden;background:var(--white)}
body{font-family:"Inter",sans-serif;color:var(--ink);position:relative}
.sheet{position:relative;width:800px;height:1200px;overflow:hidden}

/* header */
.header{position:absolute;left:0;top:0;width:800px;height:370px;background:var(--white)}
.skyline{position:absolute;right:0;top:0;width:380px;height:370px;
  background:linear-gradient(90deg,rgba(255,255,255,1) 0%,rgba(226,234,246,.6) 35%,rgba(196,212,236,.85) 100%),
  linear-gradient(180deg,#f4f7fb 0%,#c9d7ec 60%,#ffffff 100%)}
.brand{position:absolute;left:37px;top:34px;display:flex;align-items:center;gap:12px}
.brand-dot{width:46px;height:46px;border-radius:50%;background:var(--navy)}
.brand-name{font-family:"Archivo",sans-serif;font-weight:800;font-size:20px;line-height:1.05;color:var(--navy);text-transform:uppercase}
.title{position:absolute;left:37px;top:128px;font-family:"Barlow",sans-serif;font-weight:900;font-size:45px;line-height:44px;color:var(--navy-deep);letter-spacing:-.3px;text-transform:uppercase}
.subtitle{position:absolute;left:37px;top:222px;font-size:20.5px;line-height:24px;font-weight:500;color:var(--grey)}
.rule{position:absolute;height:3px;width:46px;background:var(--blue)}
.header .rule{left:37px;top:284px}
.intro{position:absolute;left:37px;top:302px;width:372px;font-size:11.6px;line-height:15.5px;color:var(--ink)}

/* pillars */
.pillars{position:absolute;left:31px;top:374px;width:738px;height:236px;display:flex;border-top:1px solid var(--line)}
.pillar{flex:1;position:relative;padding:20px 0 0 0;border-right:1px solid var(--line);background:linear-gradient(180deg,#ffffff,#f7f9fc)}
.pillar:last-child{border-right:none}
.pillar-icon{position:absolute;left:10px;top:18px;width:62px;height:62px;border-radius:50%;background:var(--navy);display:flex;align-items:center;justify-content:center}
.pillar-title{position:absolute;left:88px;top:20px;font-family:"Archivo",sans-serif;font-weight:800;font-size:15px;line-height:17px;color:var(--navy);text-transform:uppercase}
.pillar .rule{left:88px;top:78px;width:40px;height:2px}
.pillar-list{position:absolute;left:22px;top:94px;width:210px;list-style:none}
.pillar-list li{position:relative;padding-left:16px;font-size:11.6px;line-height:14px;margin-bottom:6px;color:var(--ink)}
.pillar-list li::before{content:"";position:absolute;left:2px;top:6px;width:3px;height:3px;border-radius:50%;background:var(--ink)}
.pillar-bars{position:absolute;left:33px;top:616px;width:734px;display:flex;gap:8px}
.pillar-bars span{flex:1;height:4px;background:var(--navy)}

/* snapshot */
.snapshot{position:absolute;left:0;top:634px;width:800px;height:152px;background:var(--band)}
.snapshot-label{position:absolute;left:0;top:14px;width:800px;text-align:center;font-family:"Montserrat",sans-serif;font-size:11px;font-weight:700;letter-spacing:6px;color:var(--white);text-transform:uppercase}
.snapshot-label::before,.snapshot-label::after{content:"";position:absolute;top:7px;width:45px;height:1px;background:#43506b}
.snapshot-label::before{left:220px}.snapshot-label::after{right:220px}
.stat{position:absolute;top:36px;height:87px;border:1px solid #3a4a6c;border-radius:5px;display:flex;align-items:center;gap:10px;padding-left:12px;color:var(--white);overflow:hidden}
.stat-icon{flex:none;width:42px;height:42px;border-radius:50%;border:1.5px solid var(--blue-bright);display:flex;align-items:center;justify-content:center}
.stat-value{font-family:"Archivo",sans-serif;font-weight:800;font-size:22px;line-height:23px;white-space:nowrap}
.stat-value.compact{font-size:20px}
.stat-label{font-family:"Montserrat",sans-serif;font-weight:600;font-size:11px;line-height:14px;text-transform:uppercase;margin-top:3px}
.stat-label.small{font-size:8.4px;line-height:11px}
.snapshot-note{position:absolute;left:0;top:131px;width:800px;text-align:center;font-size:9px;color:var(--muted)}

/* platform */
.platform{position:absolute;left:0;top:786px;width:800px;height:339px;background:linear-gradient(180deg,#071028,#050b1d)}
.platform-scene{position:absolute;right:0;top:0;width:480px;height:339px;
  background:radial-gradient(ellipse at 55% 40%,#1b4a9a 0%,#0c2558 40%,#050b1d 85%)}
.platform-name{position:absolute;left:37px;top:20px;font-family:"Montserrat",sans-serif;font-weight:800;font-size:32px;letter-spacing:1px;color:var(--white)}
.platform-name em{font-style:normal;color:var(--blue-bright)}
.platform-name sup{font-size:13px;vertical-align:top;position:relative;top:2px}
.platform-tag{position:absolute;left:37px;top:64px;font-size:12.8px;font-weight:500;color:var(--blue-bright)}
.platform .rule{left:37px;top:88px;width:32px;height:2px}
.platform-copy{position:absolute;left:37px;top:100px;width:290px;font-size:11.2px;line-height:14px;color:#e4e9f2}
.feature{position:absolute;left:37px;width:300px;display:flex;gap:12px}
.feature-icon{flex:none;width:43px;height:43px;border-radius:50%;border:1px solid #52617f;display:flex;align-items:center;justify-content:center}
.feature-title{font-family:"Montserrat",sans-serif;font-weight:600;font-size:11.3px;letter-spacing:.5px;color:var(--white);text-transform:uppercase;line-height:14px;margin-top:1px}
.feature-text{font-size:9.6px;line-height:13.5px;color:#c9d1df;margin-top:2px}

/* footer */
.footer{position:absolute;left:0;top:1125px;width:800px;height:75px;background:#0d2457}
.footer-motto{position:absolute;left:91px;top:25px;font-family:"Archivo",sans-serif;font-weight:800;font-size:14px;color:var(--white);text-transform:uppercase}
.footer .rule{left:91px;top:45px;width:34px;height:2px;background:var(--blue-bright)}
.footer-shield{position:absolute;left:36px;top:15px}
.footer-web{position:absolute;right:33px;top:26px;display:flex;align-items:center;gap:14px;font-family:"Montserrat",sans-serif;font-size:13.5px;font-weight:600;letter-spacing:1px;color:var(--white);text-transform:uppercase}
</style>
</head>
<body>
<main class="sheet">

  <header class="header">
    <div class="skyline" role="img" aria-label="Soft blue city skyline with a rising financial chart"></div>
    <div class="brand">
      <span class="brand-dot"></span>
      <div class="brand-name">Harbor Crest Portfolio<br>Advisors</div>
    </div>
    <h1 class="title">Master Servicing &amp;<br>Portfolio Optimization</h1>
    <p class="subtitle">End-to-End Post Default Management<br>Strategy, Recovery &amp; Compliance</p>
    <span class="rule"></span>
    <p class="intro">Harbor Crest Portfolio Advisors (HCPA) delivers integrated post default solutions designed to maximize recovery, mitigate risk, and drive long-term portfolio performance for enterprise clients.</p>
  </header>

  <section class="pillars">
    <article class="pillar">
      <div class="pillar-icon">
        <svg width="36" height="36" viewBox="0 0 36 36" fill="none" stroke="#fff" stroke-width="2"><circle cx="18" cy="18" r="12"/><circle cx="18" cy="18" r="6"/><circle cx="18" cy="18" r="1.5" fill="#fff"/><path d="M18 2v8M18 26v8M2 18h8M26 18h8"/></svg>
      </div>
      <h2 class="pillar-title">Strategy &amp;<br>Recovery<br>Optimization</h2>
      <span class="rule"></span>
      <ul class="pillar-list">
        <li>Data-driven recovery strategy development</li>
        <li>Cash flow maximization<br>&amp; loss mitigation</li>
        <li>Investor-aligned performance optimization</li>
        <li>Advanced analytics &amp; scenario modeling</li>
      </ul>
    </article>
    <article class="pillar">
      <div class="pillar-icon">
        <svg width="32" height="34" viewBox="0 0 32 34" fill="none" stroke="#fff" stroke-width="2"><path d="M16 2l12 4v10c0 8-6 13-12 16C10 29 4 24 4 16V6z"/><path d="M10 17l4 4 8-9"/></svg>
      </div>
      <h2 class="pillar-title" style="top:34px">Compliance &amp;<br>Risk Oversight</h2>
      <span class="rule"></span>
      <ul class="pillar-list">
        <li>Regulatory compliance management</li>
        <li>Policy adherence &amp; audit readiness</li>
        <li>Risk monitoring &amp; exception management</li>
        <li>Governance, controls<br>&amp; reporting</li>
      </ul>
    </article>
    <article class="pillar">
      <div class="pillar-icon">
        <svg width="36" height="36" viewBox="0 0 36 36" fill="none" stroke="#fff" stroke-width="2"><circle cx="18" cy="18" r="5"/><path d="M15 3h6l1 4 4 2 4-2 4 5-3 3v6l3 3-4 5-4-2-4 2-1 4h-6l-1-4-4-2-4 2-4-5 3-3v-6L1 12l4-5 4 2 4-2z" transform="scale(.95) translate(1 0)"/></svg>
      </div>
      <h2 class="pillar-title">Operations &amp;<br>Portfolio<br>Management</h2>
      <span class="rule"></span>
      <ul class="pillar-list">
        <li>End-to-end loan servicing oversight</li>
        <li>Vendor &amp; third-party management</li>
        <li>Payment processing<br>&amp; reconciliation</li>
        <li>Operational efficiency<br>&amp; cost optimization</li>
      </ul>
    </article>
  </section>
  <div class="pillar-bars"><span></span><span></span><span></span></div>

  <section class="snapshot">
    <h2 class="snapshot-label">Performance Snapshot</h2>
    <div class="stat" style="left:34px;width:191px">
      <div class="stat-icon"><svg width="20" height="22" viewBox="0 0 20 22" fill="none" stroke="#3d8bff" stroke-width="2"><path d="M14 6c-1-2-7-2-8 1s8 3 8 7-7 4-9 1M10 2v18"/></svg></div>
      <div><div class="stat-value">$155+<br>MILLION</div><div class="stat-label small">Recoveries generated<br>for our clients</div></div>
    </div>
    <div class="stat" style="left:234px;width:173px">
      <div class="stat-icon"><svg width="24" height="20" viewBox="0 0 24 20" fill="#3d8bff"><circle cx="12" cy="6" r="3.5"/><circle cx="5" cy="8" r="2.5"/><circle cx="19" cy="8" r="2.5"/><path d="M6 18c0-4 3-6 6-6s6 2 6 6zM0 17c0-3 2-5 5-5 1 0 2 .3 2 .5-1.5 1.5-2 3-2 4.5zM24 17c0-3-2-5-5-5-1 0-2 .3-2 .5 1.5 1.5 2 3 2 4.5z"/></svg></div>
      <div><div class="stat-value compact">573,000+</div><div class="stat-label">Accounts<br>managed</div></div>
    </div>
    <div class="stat" style="left:415px;width:165px">
      <div class="stat-icon"><svg width="22" height="18" viewBox="0 0 22 18" fill="#3d8bff"><rect x="2" y="11" width="3" height="5"/><rect x="7" y="8" width="3" height="8"/><rect x="12" y="5" width="3" height="11"/><rect x="17" y="1" width="3" height="15"/><rect x="0" y="16.5" width="22" height="1.5"/></svg></div>
      <div><div class="stat-value compact">3,700+</div><div class="stat-label" style="font-size:9.6px;line-height:13px">Investors &amp;<br>institutional<br>partners</div></div>
    </div>
    <div class="stat" style="left:589px;width:176px">
      <div class="stat-icon"><svg width="22" height="16" viewBox="0 0 22 16" fill="none" stroke="#fff" stroke-width="2"><path d="M1 14l6-6 4 4 9-9M14 3h6v6"/></svg></div>
      <div><div class="stat-value">21%</div><div class="stat-label">Average net<br>recovery lift</div></div>
    </div>
    <p class="snapshot-note">Results represent cumulative performance across managed portfolios.</p>
  </section>

  <section class="platform">
    <div class="platform-scene" role="img" aria-label="Analyst seated before a wall of glowing blue compliance and analytics dashboards"></div>
    <h2 class="platform-name">CLEARPATH<em>IQ</em><sup>™</sup></h2>
    <p class="platform-tag">The Intelligence Behind Every Compliant Command.</p>
    <span class="rule"></span>
    <p class="platform-copy">ClearPathIQ™ is HCPA’s proprietary technology platform built to power intelligent decision-making, automate complex workflows, and deliver real-time insight across the entire post default lifecycle.</p>
    <div class="feature" style="top:168px">
      <div class="feature-icon"><svg width="20" height="22" viewBox="0 0 32 34" fill="none" stroke="#fff" stroke-width="2.4"><path d="M16 2l12 4v10c0 8-6 13-12 16C10 29 4 24 4 16V6z"/><path d="M10 17l4 4 8-9"/></svg></div>
      <div><div class="feature-title">Built-in Compliance Controls</div><div class="feature-text">Embedded policies and real-time monitoring<br>ensure regulatory confidence.</div></div>
    </div>
    <div class="feature" style="top:219px">
      <div class="feature-icon"><svg width="18" height="20" viewBox="0 0 18 20" fill="none" stroke="#fff" stroke-width="1.6"><ellipse cx="9" cy="4" rx="7" ry="2.5"/><path d="M2 4v12c0 1.4 3 2.5 7 2.5s7-1.1 7-2.5V4M2 8c0 1.4 3 2.5 7 2.5s7-1.1 7-2.5M2 12c0 1.4 3 2.5 7 2.5s7-1.1 7-2.5"/></svg></div>
      <div><div class="feature-title">Centralized Asset Visibility</div><div class="feature-text">Unified data. Complete transparency.<br>Smarter decisions.</div></div>
    </div>
    <div class="feature" style="top:270px">
      <div class="feature-icon"><svg width="22" height="20" viewBox="0 0 22 20" fill="none" stroke="#fff" stroke-width="1.6"><circle cx="8" cy="12" r="4"/><circle cx="8" cy="12" r="1.5"/><path d="M8 6v-2M8 20v-2M2 12H0M16 12h-2M3.8 7.8L2.4 6.4M13.6 17.6l-1.4-1.4M3.8 16.2l-1.4 1.4M13.6 6.4l-1.4 1.4"/><circle cx="17" cy="5" r="2.5"/><path d="M17 1v1M17 8v1M13 5h1M20 5h1"/></svg></div>
      <div><div class="feature-title">Automated Workflow &amp;<br>Recovery Execution</div><div class="feature-text">Intelligent automation that drives efficiency,<br>accuracy, and outcomes.</div></div>
    </div>
  </section>

  <footer class="footer">
    <svg class="footer-shield" width="40" height="46" viewBox="0 0 32 34" fill="none" stroke="#fff" stroke-width="2.4"><path d="M16 2l12 4v10c0 8-6 13-12 16C10 29 4 24 4 16V6z"/><path d="M10 17l4 4 8-9"/></svg>
    <p class="footer-motto">Your Trusted Advisor.</p>
    <span class="rule"></span>
    <div class="footer-web">
      <svg width="26" height="26" viewBox="0 0 26 26" fill="none" stroke="#fff" stroke-width="1.5"><circle cx="13" cy="13" r="11"/><ellipse cx="13" cy="13" rx="5" ry="11"/><path d="M2 13h22M4 7h18M4 19h18"/></svg>
      <span>harborcrestadvisors.com</span>
    </div>
  </footer>

</main>
</body>
</html>
```